QUILLDESK - Remote Tech Support Site

We are looking for a new very responsive and simple website for our brand Quilldesk.com - a remote technical support company.

This company supports customers Globally in different countries throughout Eur/ North America / South America / Asia etc (please keep this in mind and integrate into the idea).

Its important to us that the design is very explanatory, the customer should easily be able to figure out that we provide computer support right away ... I like one page responsive type designs as well without a bunch of menu items

Here are some similar sites we like - but still looking for a unique design that fits out brand "quilldesk" - I have upload also some layouts i like (but the designs are not important just the layouts), youll see it includes consumer business etc which is important.

MORVEL.COM - I love how clean it is - nice and white easy to see everything

PIXOLANE247.COM - also nice the layout and responsive one page design makes it easy to use

brightfixhub.com - similar to pixolane design as well - you can get the idea im looking for between the two

You will notice those examples are much different then the attachments I added - again this is more of an idea for possible layouts .. attached is also the logo - could inspire color scheme / blue white black etc

Target Market(s)

Home consumers without computer knowledge , older age 45-65, small medium business ... computer repair - slow computers

Industry/Entity Type

Computer Repair

Logo Text

Quilldesk

Coding

Coded - Design and coding required

Number of Pages Required

1 page

Font styles to use
Sans Serif
Other font styles liked:
• your choice responsive

Colors

Designer to choose colors to be used in the design.

Requirements
Must have
• Clean - responsive - professional design - the name says it all - quilldesk
• CALL TO ACTIONS FOR "Get Help Now!" / "Learn More" etc
Nice to have
• We are looking for a new very responsive and simple website for our brand Quilldesk.com - a remote technical support company.
• This company supports customers Globally in different countries throughout Eur/ North America / South America / Asia etc (please keep this in mind and integrate into the idea).
• Its important to us that the design is very explanatory, the customer should easily be able to figure out that we provide computer support right away ... I like one page responsive type designs as well without a bunch of menu items
• Here are some similar sites we like - but still looking for a unique design that fits out brand "quilldesk" - I have upload also some layouts i like (but the designs are not important just the layouts), youll see it includes consumer business etc which is important.
• MORVEL.COM - I love how clean it is - nice and white easy to see everything
• PIXOLANE247.COM - also nice the layout and responsive one page design makes it easy to use
• brightfixhub.com - similar to pixolane design as well - you can get the idea im looking for between the two
Should not have
• dark, packed page - bad small font -

```html
<!DOCTYPE html>
<html lang="en">
<head>
<meta charset="utf-8">
<title>Quilldesk – Remote Tech Support</title>
<link href="https://fonts.googleapis.com/css2?family=Open+Sans:wght@400;600;700&display=swap" rel="stylesheet">
<style>
:root{
  --blue:#1e8ae6;
  --blue-dark:#1677cf;
  --navy:#23262f;
  --ink:#2b2b2b;
  --text:#5a5a5a;
  --muted:#777;
  --line:#e2e2e2;
  --panel:#f3f3f3;
  --footer:#333333;
  --white:#ffffff;
}
*{box-sizing:border-box;margin:0;padding:0}
html,body{width:1200px;height:2757px;overflow:hidden}
body{font-family:"Open Sans",Arial,sans-serif;color:var(--text);background:var(--white);position:relative}
.abs{position:absolute}
section,header,footer{position:absolute;left:0;width:1200px}

/* header */
.site-header{top:0;height:96px;background:var(--navy)}
.brand{left:132px;top:26px;display:flex;align-items:center;gap:10px;color:var(--white);font-size:34px;font-weight:600;letter-spacing:-.5px}
.brand-dot{width:44px;height:44px;border-radius:50%;background:var(--blue)}
.nav{top:38px;font-size:14px;color:#e6e6e6}
.nav.active{color:var(--blue)}
.login{left:926px;top:29px;width:74px;height:37px;border:1px solid #c9c9c9;border-radius:3px;color:#eee;font-size:13px;display:flex;align-items:center;justify-content:center}
.cart{left:1030px;top:30px;width:36px;height:36px;border-radius:50%;background:#000;display:flex;align-items:center;justify-content:center}
.cart-count{position:absolute;top:3px;font-size:9px;color:#fff}

/* info bar */
.info-bar{top:96px;height:64px;background:var(--white);border-bottom:1px solid var(--line)}
.info{top:22px;font-size:15px;color:#555;display:flex;align-items:center;gap:8px;transform:translateX(-50%)}

/* hero */
.hero{top:160px;height:454px}
.hero-photo{inset:0;background:linear-gradient(100deg,#d9dadc 0%,#eceded 35%,#f2f2f2 55%,#e5e5e6 100%)}
.hero-title{top:88px;width:100%;text-align:center;color:var(--blue);font-size:43px;font-weight:700;letter-spacing:.5px}
.hero-sub{top:136px;width:100%;text-align:center;color:#3d3d3d;font-size:35px;font-weight:400}
.btn{position:absolute;background:var(--blue);color:#fff;font-weight:600;display:flex;align-items:center;justify-content:center;border-radius:2px}
.hero .btn{top:193px;height:46px;font-size:16px}
.slide-arrow{top:212px;width:28px;height:28px;border-radius:50%;background:#555;opacity:.75;display:flex;align-items:center;justify-content:center}

/* section titles */
.section-title{width:100%;text-align:center;color:var(--blue);font-size:27px;font-weight:700}

/* how it works */
.how{top:614px;height:415px;border-bottom:1px solid var(--line)}
.how .section-title{top:73px}
.step{top:125px;width:287px;height:211px;border:2px solid #e6e6e6;text-align:center}
.step svg{position:absolute;left:50%;top:25px;transform:translateX(-50%)}
.step-title{position:absolute;top:92px;width:100%;color:var(--blue);font-size:20px;font-weight:400}
.step-text{position:absolute;top:126px;left:30px;right:30px;font-size:12px;line-height:18px;color:var(--muted)}

/* features */
.features{top:1029px;height:307px}
.features .section-title{top:56px}
.feature{font-size:15px;color:#555;display:flex;align-items:center;gap:11px}
.tick{width:13px;height:13px}

/* products */
.products{top:1336px;height:726px;background:var(--panel)}
.products .section-title{top:90px}
.product-box{top:153px;width:130px;height:126px}
.product-card{top:285px;height:355px;background:var(--white);box-shadow:0 1px 4px rgba(0,0,0,.12);text-align:center}
.product-name{position:absolute;top:68px;width:100%;font-size:19px;font-weight:600;color:#111}
.product-price{position:absolute;top:98px;width:100%;font-size:29px;font-weight:700;color:var(--blue)}
.product-fee{position:absolute;top:143px;width:100%;font-size:14px;color:#333}
.product-perks{position:absolute;top:183px;width:100%;font-size:13px;line-height:21px;color:#444}
.product-card .btn{left:50%;transform:translateX(-50%);top:270px;width:158px;height:48px;font-size:16px}

/* call */
.call{top:2062px;height:423px}
.call-video{left:132px;top:52px;width:464px;height:320px;background:linear-gradient(135deg,#8a5a3c 0%,#6f4a34 45%,#3f3a3a 100%)}
.play{left:348px;top:200px;width:48px;height:48px;border-radius:50%;background:#fff;display:flex;align-items:center;justify-content:center}
.call-panel{left:605px;top:52px;width:461px;height:320px;background:#f1f1f1;text-align:center}
.call-title{position:absolute;top:52px;width:100%;color:var(--blue);font-size:28px;font-weight:700}
.call-sub{position:absolute;top:100px;width:100%;font-size:19px;color:#222}
.call-note{position:absolute;top:142px;width:100%;font-size:13px;line-height:24px;color:#444}
.call-panel .btn{left:150px;top:213px;width:160px;height:44px;font-size:16px}

/* footer */
.site-footer{top:2485px;height:272px;background:var(--footer);color:#ccc}
.f-title{top:50px;font-size:16px;color:#eee}
.newsletter{left:132px;top:81px;width:217px;height:39px;background:#fff;font-size:11px;color:#333;display:flex;align-items:center;justify-content:space-between;padding:0 14px}
.social{top:147px;width:24px;height:24px;border-radius:50%;background:#d9d9d9}
.f-links{left:472px;top:82px;font-size:11px;line-height:19px;color:#bbb;list-style:none}
.f-links li::before{content:"• ";color:#999}
.f-contact{left:619px;top:82px;font-size:11px;line-height:18px;color:#bbb}
.badge-rating{left:946px;top:48px;width:120px;height:47px;background:#fff;border-radius:4px}
.badge-medal{left:900px;top:105px;width:64px;height:58px;border-radius:50%;background:radial-gradient(circle,#f2c744 0%,#c9911c 70%,#8a6512 100%)}
.badge-secure{left:986px;top:110px;width:80px;height:52px;background:#d22b2b;border-radius:4px}
.f-rule{left:0;top:208px;width:1200px;height:1px;background:#4a4a4a}
.copyright{top:231px;width:100%;text-align:center;font-size:11px;color:#aaa}
</style>
</head>
<body>

<header class="site-header">
  <div class="abs brand"><span class="brand-dot"></span>quilldesk</div>
  <span class="abs nav active" style="left:522px">Home</span>
  <span class="abs nav" style="left:593px">About Us</span>
  <span class="abs nav" style="left:682px">Services</span>
  <span class="abs nav" style="left:765px">Contact Us</span>
  <span class="abs nav" style="left:862px">FAQs</span>
  <span class="abs login">Log in</span>
  <span class="abs cart"><span class="cart-count">0</span>
    <svg width="14" height="12" viewBox="0 0 14 12"><path d="M0 1h3l2 7h7l2-5H4" fill="none" stroke="#fff" stroke-width="1.5"/><circle cx="6" cy="10.5" r="1.2" fill="#fff"/><circle cx="11" cy="10.5" r="1.2" fill="#fff"/></svg>
  </span>
</header>

<section class="info-bar">
  <span class="abs info" style="left:294px">
    <svg width="14" height="10" viewBox="0 0 14 10"><rect width="14" height="10" fill="#666"/><path d="M0 0l7 6 7-6" fill="none" stroke="#fff" stroke-width="1"/></svg>info@quilldesk.com</span>
  <span class="abs info" style="left:597px">
    <svg width="8" height="13" viewBox="0 0 8 13"><rect x=".5" y=".5" width="7" height="12" rx="1" fill="none" stroke="#666"/><rect x="2" y="2" width="4" height="7" fill="#666"/></svg>(800) 555-0142</span>
  <span class="abs info" style="left:912px">
    <svg width="13" height="13" viewBox="0 0 13 13"><circle cx="6.5" cy="6.5" r="6" fill="#666"/><path d="M1 6.5h11M6.5 1c-3 3-3 8 0 11M6.5 1c3 3 3 8 0 11" fill="none" stroke="#fff" stroke-width=".8"/></svg>United States - EN</span>
</section>

<section class="hero">
  <div class="abs hero-photo" role="img" aria-label="Photo of a young man working at a laptop in a bright office with bookshelves"></div>
  <h1 class="abs hero-title">DEDICATED SUPPORT</h1>
  <p class="abs hero-sub">Anytime.&nbsp; Anywhere.</p>
  <a class="btn" style="left:430px;width:162px">Get Help Now!</a>
  <a class="btn" style="left:610px;width:156px">Learn More</a>
  <span class="abs slide-arrow" style="left:22px"><svg width="8" height="12" viewBox="0 0 8 12"><path d="M6 1L1 6l5 5" fill="none" stroke="#fff" stroke-width="2"/></svg></span>
  <span class="abs slide-arrow" style="left:1146px"><svg width="8" height="12" viewBox="0 0 8 12"><path d="M2 1l5 5-5 5" fill="none" stroke="#fff" stroke-width="2"/></svg></span>
</section>

<section class="how">
  <h2 class="abs section-title">HOW IT WORKS</h2>
  <div class="abs step" style="left:132px">
    <svg width="56" height="56" viewBox="0 0 56 56"><circle cx="21" cy="21" r="15" fill="none" stroke="#1e8ae6" stroke-width="3"/><path d="M32 32l18 18" stroke="#1e8ae6" stroke-width="5" stroke-linecap="round"/></svg>
    <h3 class="step-title">FREE Diagnostic</h3>
    <p class="step-text">Get a diagnostic, FOR FREE! Get a free consultation with our staff.</p>
  </div>
  <div class="abs step" style="left:456px">
    <svg width="56" height="56" viewBox="0 0 56 56"><path d="M8 48L36 20M14 6a10 10 0 0 0 8 16L46 46l4-4-24-24A10 10 0 0 0 12 8l6 6-4 4-6-6" fill="none" stroke="#1e8ae6" stroke-width="3" stroke-linejoin="round"/><path d="M36 20l6-6 4 2 4-8-4-2-6 6 2 4" fill="none" stroke="#1e8ae6" stroke-width="3"/></svg>
    <h3 class="step-title">Get Fixed</h3>
    <p class="step-text">Get fixed, IMMEDIATELY! Our staff will solve your computer issues right before your eyes.</p>
  </div>
  <div class="abs step" style="left:779px">
    <svg width="56" height="56" viewBox="0 0 56 56"><path d="M16 6h20l10 10v34H16z" fill="#fff" stroke="#1e8ae6" stroke-width="3"/><path d="M10 12v40h28" fill="none" stroke="#1e8ae6" stroke-width="3"/><path d="M22 22h18M22 29h18M22 36h18M22 43h12" stroke="#1e8ae6" stroke-width="2.5"/></svg>
    <h3 class="step-title">Backup your information!</h3>
    <p class="step-text">Saving your files is now EASY! You will be able to retain your personal files without any loss of data.</p>
  </div>
</section>

<section class="features">
  <h2 class="abs section-title">REAL-TIME SUPPORT FEATURES AND BENEFITS</h2>
  <ul style="list-style:none">
    <li class="abs feature" style="left:132px;top:112px"><svg class="tick" viewBox="0 0 13 13"><circle cx="6.5" cy="6.5" r="5.5" fill="none" stroke="#555" stroke-width="1.4"/><path d="M4 6.5l2 2 3.3-3.5" fill="none" stroke="#555" stroke-width="1.4"/></svg>24/7 Real-Time Technician Support</li>
    <li class="abs feature" style="left:132px;top:145px"><svg class="tick" viewBox="0 0 13 13"><circle cx="6.5" cy="6.5" r="5.5" fill="none" stroke="#555" stroke-width="1.4"/><path d="M4 6.5l2 2 3.3-3.5" fill="none" stroke="#555" stroke-width="1.4"/></svg>The best Security Software in the market</li>
    <li class="abs feature" style="left:132px;top:177px"><svg class="tick" viewBox="0 0 13 13"><circle cx="6.5" cy="6.5" r="5.5" fill="none" stroke="#555" stroke-width="1.4"/><path d="M4 6.5l2 2 3.3-3.5" fill="none" stroke="#555" stroke-width="1.4"/></svg>Regular tune-ups and optimization</li>
    <li class="abs feature" style="left:132px;top:208px"><svg class="tick" viewBox="0 0 13 13"><circle cx="6.5" cy="6.5" r="5.5" fill="none" stroke="#555" stroke-width="1.4"/><path d="M4 6.5l2 2 3.3-3.5" fill="none" stroke="#555" stroke-width="1.4"/></svg>Setup and installation included</li>
    <li class="abs feature" style="left:572px;top:112px"><svg class="tick" viewBox="0 0 13 13"><circle cx="6.5" cy="6.5" r="5.5" fill="none" stroke="#555" stroke-width="1.4"/><path d="M4 6.5l2 2 3.3-3.5" fill="none" stroke="#555" stroke-width="1.4"/></svg>Instant Support</li>
    <li class="abs feature" style="left:572px;top:145px"><svg class="tick" viewBox="0 0 13 13"><circle cx="6.5" cy="6.5" r="5.5" fill="none" stroke="#555" stroke-width="1.4"/><path d="M4 6.5l2 2 3.3-3.5" fill="none" stroke="#555" stroke-width="1.4"/></svg>Real-Time Optimization</li>
    <li class="abs feature" style="left:572px;top:177px"><svg class="tick" viewBox="0 0 13 13"><circle cx="6.5" cy="6.5" r="5.5" fill="none" stroke="#555" stroke-width="1.4"/><path d="M4 6.5l2 2 3.3-3.5" fill="none" stroke="#555" stroke-width="1.4"/></svg>Free Diagnostic</li>
    <li class="abs feature" style="left:572px;top:208px"><svg class="tick" viewBox="0 0 13 13"><circle cx="6.5" cy="6.5" r="5.5" fill="none" stroke="#555" stroke-width="1.4"/><path d="M4 6.5l2 2 3.3-3.5" fill="none" stroke="#555" stroke-width="1.4"/></svg>Quick Setup &amp; Install</li>
    <li class="abs feature" style="left:871px;top:112px"><svg class="tick" viewBox="0 0 13 13"><circle cx="6.5" cy="6.5" r="5.5" fill="none" stroke="#555" stroke-width="1.4"/><path d="M4 6.5l2 2 3.3-3.5" fill="none" stroke="#555" stroke-width="1.4"/></svg>Leading Security Software</li>
    <li class="abs feature" style="left:871px;top:145px"><svg class="tick" viewBox="0 0 13 13"><circle cx="6.5" cy="6.5" r="5.5" fill="none" stroke="#555" stroke-width="1.4"/><path d="M4 6.5l2 2 3.3-3.5" fill="none" stroke="#555" stroke-width="1.4"/></svg>Unlimited Cloud Backup</li>
  </ul>
</section>

<section class="products">
  <h2 class="abs section-title">OUR PRODUCTS</h2>

  <div class="abs product-box" style="left:216px;background:linear-gradient(90deg,#2a2a2a 0%,#2a2a2a 22%,#9a9a9a 40%,#d8d8d8 100%)" role="img" aria-label="Software box for the Premium plan"></div>
  <div class="abs product-box" style="left:536px;background:linear-gradient(90deg,#1d3f66 0%,#1d3f66 22%,#3f7fc0 45%,#9cc6ea 100%)" role="img" aria-label="Software box for the Premium Plus plan"></div>
  <div class="abs product-box" style="left:852px;background:linear-gradient(90deg,#8a0f12 0%,#8a0f12 22%,#d52a24 45%,#e8514a 100%)" role="img" aria-label="Software box for the Platinum plan"></div>

  <div class="abs product-card" style="left:132px;width:298px">
    <h3 class="product-name">PREMIUM</h3>
    <p class="product-price">$19.99MONTHLY</p>
    <p class="product-fee">($249-$300 SETUP FEE)</p>
    <p class="product-perks">Regular 90-Day Optimization<br>Unlimited 24/7 Tier 3 Technician Support</p>
    <a class="btn">Add to cart</a>
  </div>
  <div class="abs product-card" style="left:452px;width:296px">
    <h3 class="product-name">PREMIUM PLUS</h3>
    <p class="product-price">$29.99MONTHLY</p>
    <p class="product-fee">($249-$300 SETUP FEE)</p>
    <p class="product-perks">Regular 90-Day Optimization<br>Unlimited 24/7 Tier 3 Technician Support</p>
    <a class="btn">Add to cart</a>
  </div>
  <div class="abs product-card" style="left:770px;width:296px">
    <h3 class="product-name">PLATINUM</h3>
    <p class="product-price">$39.99MONTHLY</p>
    <p class="product-fee">($249-$300 SETUP FEE)</p>
    <p class="product-perks">Regular 90-Day Optimization<br>Unlimited 24/7 Tier 3 Technician Support<br>Online Identity Theft Protection</p>
    <a class="btn">Add to cart</a>
  </div>
</section>

<section class="call">
  <div class="abs call-video" role="img" aria-label="Animated video still of a support agent at a desk with a computer and coffee cup"></div>
  <span class="abs play" style="left:348px;top:203px"><svg width="16" height="18" viewBox="0 0 16 18"><path d="M2 1l13 8-13 8z" fill="#333"/></svg></span>
  <div class="abs call-panel">
    <h2 class="call-title">CALL US TODAY</h2>
    <p class="call-sub">And get started with our dedicated technicians.</p>
    <p class="call-note">Get a 30-minute one-on-one free consultation with one of our experts! *<br>*Limited period offer</p>
    <a class="btn">Learn More</a>
  </div>
</section>

<footer class="site-footer">
  <h4 class="abs f-title" style="left:132px">Newsletter Signup</h4>
  <div class="abs newsletter"><span>Email Address</span>
    <svg width="13" height="10" viewBox="0 0 13 10"><rect width="13" height="10" fill="#777"/><path d="M0 0l6.5 5.5L13 0" fill="none" stroke="#fff"/></svg></div>
  <span class="abs social" style="left:133px"></span>
  <span class="abs social" style="left:161px"></span>
  <span class="abs social" style="left:189px"></span>
  <span class="abs social" style="left:217px"></span>
  <span class="abs social" style="left:245px"></span>
  <span class="abs social" style="left:273px"></span>

  <h4 class="abs f-title" style="left:472px">Links</h4>
  <ul class="abs f-links">
    <li>Home</li><li>About Us</li><li>Services</li><li>Contact Us</li><li>FAQs</li>
  </ul>

  <h4 class="abs f-title" style="left:619px">Contact Us</h4>
  <p class="abs f-contact">Norlen Ltd, 48 Harbour Ave. 2nd Floor,<br>Halifax, NS B3K 2P4 Canada<br><br>(800) 555-0142<br><br>info@quilldesk.com</p>

  <span class="abs badge-rating"></span>
  <span class="abs badge-medal"></span>
  <span class="abs badge-secure"></span>

  <span class="abs f-rule"></span>
  <p class="abs copyright">Copyright &copy; 2017 Quilldesk.&nbsp;&nbsp; All rights reserved.</p>
</footer>

</body>
</html>
```